Oil Field Service company needs professional business cards

Looking to clean up our current company business cards and look a little more professional. Harlow Casing Services is a US based company that services the oil field. We deal with engineers, managers and oil rigs....................................................................................................................................................................................................................................................................................................................................................................................................

Target Market(s)

Oil and Gas professionals

Industry/Entity Type

Oil And Gas

Contact Information for Business Card

See attached photo as example

Font styles to use
Sans Serif

Colors
ec1f27

Requirements
Must have
• Company Logo, Name, Title, Cell, Office, Fax, Email.
• See attached photo
Nice to have
• External CRT, Internal CRT, Casing Crews, Torque Turn, Laydown Machine
Should not have
• Do not introduce any new pictures and keep it professional looking

```html
<!DOCTYPE html>
<html lang="en">
<head>
<meta charset="UTF-8">
<title>Harlow Casing Services – Business Card</title>
<link href="https://fonts.googleapis.com/css2?family=Open+Sans:wght@400;600;700&display=swap" rel="stylesheet">
<style>
  :root {
    --stage: #000000;
    --card-light: #f2f2f2;
    --card-dark: #465560;
    --slate: #3b4650;
    --ink: #2b2f33;
    --brand-red: #ec1f27;
    --white: #ffffff;
  }
  * { margin: 0; padding: 0; box-sizing: border-box; }
  html, body {
    width: 1200px; height: 900px; overflow: hidden;
    background: var(--stage);
    font-family: "Open Sans", Arial, sans-serif;
  }
  .stage { position: relative; width: 1200px; height: 900px; }

  .card { position: absolute; top: 200px; width: 310px; height: 502px; }
  .card--front {
    left: 265px; background: var(--card-light);
    border-radius: 56px 0 56px 0;
  }
  .card--back {
    left: 641px; width: 308px; background: var(--card-dark);
    border-radius: 0 56px 0 56px;
  }

  .wordmark { position: absolute; left: 0; right: 0; text-align: center; font-weight: 700; }
  .wordmark__name { display: block; font-size: 42px; letter-spacing: 3px; line-height: 1; }
  .wordmark__tagline { display: block; font-size: 14px; letter-spacing: 3.2px; margin-top: 12px; }
  .card--front .wordmark { top: 66px; color: var(--slate); }
  .card--back .wordmark { top: 362px; color: var(--white); }

  .person { position: absolute; left: 24px; top: 332px; }
  .person__name { font-size: 17px; font-weight: 600; color: var(--slate); line-height: 1.2; }
  .person__first { color: var(--brand-red); }
  .person__title { font-size: 13px; color: var(--ink); margin-top: 1px; }

  .contacts { position: absolute; left: 24px; top: 398px; list-style: none; }
  .contacts__item {
    display: flex; align-items: center; height: 18px;
    font-size: 13px; color: var(--ink);
  }
  .contacts__icon { width: 10px; height: 10px; margin-right: 8px; fill: var(--brand-red); flex: none; }
</style>
</head>
<body>
<main class="stage">
  <section class="card card--front" aria-label="Card front">
    <div class="wordmark">
      <span class="wordmark__name">HARLOW</span>
      <span class="wordmark__tagline">CASING SERVICES</span>
    </div>

    <div class="person">
      <p class="person__name"><span class="person__first">Wade</span> Corrigan</p>
      <p class="person__title">Area Manager</p>
    </div>

    <ul class="contacts">
      <li class="contacts__item">
        <svg class="contacts__icon" viewBox="0 0 10 10" aria-hidden="true"><path d="M2 0.5 L3.6 2.6 L2.7 3.7 Q3.8 5.9 6.3 7.3 L7.4 6.4 L9.5 8 L8.4 9.5 Q4.6 9.3 2.1 6.5 Q0.4 4.4 0.5 1.6 Z"/></svg>
        (058) 417-2200
      </li>
      <li class="contacts__item">
        <svg class="contacts__icon" viewBox="0 0 10 10" aria-hidden="true"><path d="M2.5 0 H7.5 V10 H2.5 Z M3.4 1.2 V7.8 H6.6 V1.2 Z M4.5 8.4 H5.5 V9.2 H4.5 Z"/></svg>
        (580) 619-3084
      </li>
      <li class="contacts__item">
        <svg class="contacts__icon" viewBox="0 0 10 10" aria-hidden="true"><path d="M2.5 0.5 H7 V3.5 H2.5 Z M0.5 4 H9.5 V9.5 H0.5 Z M2 6 H4.5 V7.2 H2 Z M6 5.5 H8 V6.3 H6 Z M6 7 H8 V7.8 H6 Z"/></svg>
        (580) 417-2251
      </li>
      <li class="contacts__item">
        <svg class="contacts__icon" viewBox="0 0 10 10" aria-hidden="true"><path d="M0.5 2 H9.5 V8.5 H0.5 Z" /><path d="M0.8 2.3 L5 5.6 L9.2 2.3" fill="none" stroke="#f2f2f2" stroke-width="0.9"/></svg>
        wade.corrigan@harlowmail.com
      </li>
    </ul>
  </section>

  <section class="card card--back" aria-label="Card back">
    <div class="wordmark">
      <span class="wordmark__name">HARLOW</span>
      <span class="wordmark__tagline">CASING SERVICES</span>
    </div>
  </section>
</main>
</body>
</html>
```